Thumbnail for "Exclusive Shows"

I need a Thumbnail / Cover for exclusive shows I'll upload to sonawharf. It should be unique and especially made for this purpose. My channel delivers electronic dance music and thus should be seen in the thumbnail / cover. There will be now attached files so there is nothing to influence you in your work.

Target Market(s)

Young people enjoying electronic dance music

Colors
e667a6
876aae
f04a50
f68d4d
33a6d7
3176b5

Requirements
Must have
• The design should include my logo (which will be the only thing provided later this day).
Nice to have
• Would it be good to keep it simple with texting. If you want to integrate the word "Exclusive" or "Exclusive Show" it will fit as long as it's fit to the whole design.

```html
<!DOCTYPE html>
<html lang="en">
<head>
<meta charset="utf-8">
<title>Tidemark – Exclusive Show cover</title>
<link rel="stylesheet" href="https://fonts.googleapis.com/css2?family=Exo+2:wght@700;800&display=swap">
<style>
  :root {
    --navy: #252a47;
    --navy-deep: #1c2140;
    --pink: #e667a6;
    --violet: #876aae;
    --red: #f04a50;
    --orange: #f68d4d;
    --sky: #33a6d7;
    --blue: #3176b5;
    --white: #ffffff;
  }
  html, body {
    margin: 0;
    padding: 0;
    overflow: hidden;
    background: var(--navy);
  }
  .cover {
    position: relative;
    width: 1200px;
    height: 304px;
    overflow: hidden;
    background: var(--navy);
    font-family: "Exo 2", "Arial Narrow", sans-serif;
  }
  .grid-texture {
    position: absolute;
    inset: 0;
    background:
      linear-gradient(90deg,
        rgba(240, 74, 80, 0.30) 0%,
        rgba(240, 74, 80, 0.22) 22%,
        rgba(135, 106, 174, 0.22) 45%,
        rgba(49, 118, 181, 0.22) 62%,
        rgba(135, 106, 174, 0.22) 82%,
        rgba(240, 74, 80, 0.26) 100%);
    -webkit-mask-image: linear-gradient(180deg, #000 0%, #000 55%, transparent 95%);
    mask-image: linear-gradient(180deg, #000 0%, #000 55%, transparent 95%);
  }
  .energy-glow {
    position: absolute;
    left: 330px;
    top: 150px;
    width: 540px;
    height: 300px;
    border-radius: 50%;
    background: radial-gradient(ellipse at 50% 75%,
      rgba(220, 245, 255, 0.95) 0%,
      rgba(51, 166, 215, 0.85) 18%,
      rgba(49, 118, 181, 0.55) 42%,
      rgba(49, 118, 181, 0) 70%);
  }
  .streaks {
    position: absolute;
    inset: 0;
  }
  .brand-name {
    position: absolute;
    left: 0;
    right: 0;
    top: 108px;
    margin: 0;
    text-align: center;
    font-size: 72px;
    font-weight: 800;
    letter-spacing: 6px;
    line-height: 1;
    color: var(--white);
    text-transform: uppercase;
  }
  .show-tag {
    position: absolute;
    left: 0;
    right: 0;
    top: 214px;
    margin: 0;
    text-align: center;
    font-size: 33px;
    font-weight: 700;
    line-height: 1;
    color: var(--white);
    -webkit-text-stroke: 1px var(--violet);
    text-shadow: 0 0 6px var(--violet), 0 0 2px var(--violet);
  }
</style>
</head>
<body>
  <main class="cover">
    <div class="grid-texture" role="img" aria-label="Field of small outlined squares fading from red on the left through violet and blue to red on the right"></div>
    <div class="energy-glow" role="img" aria-label="Bright blue electric burst with lightning rising from the bottom centre"></div>

    <svg class="streaks" width="1200" height="304" viewBox="0 0 1200 304" aria-hidden="true">
      <g stroke-linecap="round">
        <line x1="-10" y1="200" x2="200" y2="90" stroke="var(--sky)" stroke-width="5"/>
        <line x1="-10" y1="238" x2="270" y2="78" stroke="var(--orange)" stroke-width="4"/>
        <line x1="-10" y1="262" x2="280" y2="96" stroke="var(--red)" stroke-width="5"/>
        <line x1="20" y1="300" x2="250" y2="160" stroke="var(--sky)" stroke-width="5"/>
        <line x1="100" y1="310" x2="240" y2="225" stroke="var(--orange)" stroke-width="3"/>
        <line x1="120" y1="290" x2="160" y2="266" stroke="var(--sky)" stroke-width="3"/>

        <line x1="900" y1="240" x2="1200" y2="38" stroke="var(--sky)" stroke-width="5"/>
        <line x1="810" y1="270" x2="1160" y2="20" stroke="var(--orange)" stroke-width="4"/>
        <line x1="930" y1="262" x2="1200" y2="80" stroke="var(--sky)" stroke-width="4"/>
        <line x1="1050" y1="200" x2="1200" y2="98" stroke="var(--red)" stroke-width="5"/>
        <line x1="1040" y1="230" x2="1200" y2="118" stroke="var(--red)" stroke-width="3"/>
        <line x1="1110" y1="10" x2="1200" y2="-40" stroke="var(--sky)" stroke-width="4"/>
      </g>
    </svg>

    <h1 class="brand-name">Tidemark</h1>
    <p class="show-tag">"EXCLUSIVE SHOW"</p>
  </main>
</body>
</html>
```